Beekeeping company in need of a new attractive, simple website

We need a simple website for our Company 'Tarnfield Hives LLC' that will feature a couple different products that we offer (2019 NUCS & 2019 Queens) with the ability for customers to place orders for those products. Products will be for pickup only on specific dates so no shipping is required but will need dropdown menus to select which dates with limited quantities each date. Payments can be made through Paypal, Wix, and Square. Need the to ability to add and remove products from view on the site while maintaining information. Would like the ability to build a mailing list of potential customers and also connect visitors to our social media sites.
Beekeepers,

```html
<!DOCTYPE html>
<html lang="en">
<head>
<meta charset="utf-8">
<title>Tarnfield Hives LLC</title>
<link href="https://fonts.googleapis.com/css2?family=Anton&family=Montserrat:wght@400;500;600;700&family=Overlock:wght@700;900&display=swap" rel="stylesheet">
<style>
:root{
  --orange:#f59c0d;
  --orange-dark:#c8860a;
  --ink:#222;
  --muted:#8a8a8a;
  --dark:#3a3835;
  --olive:#735a0c;
  --paper:#f6f6f6;
  --white:#fff;
  --tick:#8a6410;
}
*{box-sizing:border-box;margin:0;padding:0}
html,body{width:1200px;height:3232px;overflow:hidden}
body{font-family:'Montserrat',sans-serif;color:var(--ink);background:var(--white);position:relative}
section,header,footer{position:absolute;left:0;width:1200px}
.abs{position:absolute}
.center{left:0;width:1200px;text-align:center}

/* hero */
.hero{top:0;height:653px;overflow:hidden}
.hero-photo{position:absolute;inset:0;background:
  radial-gradient(ellipse at 30% 70%,rgba(200,140,40,.55),transparent 55%),
  radial-gradient(ellipse at 80% 40%,rgba(230,200,150,.5),transparent 50%),
  linear-gradient(180deg,#2e2a25 0%,#5a4530 18%,#8a6a45 55%,#6b4e2e 100%)}
.phone{left:130px;top:26px;color:var(--white);font-size:13px;display:flex;align-items:center;gap:10px}
.wordmark{font-family:'Montserrat',sans-serif;font-weight:700;color:var(--white);text-transform:uppercase;letter-spacing:1px}
.brand{top:74px;left:0;width:1200px;text-align:center;font-size:22px;line-height:26px}
.nav{top:155px;display:flex;justify-content:center;gap:26px;color:var(--white);font-size:13px;font-weight:600}
.nav span.sep{color:#ddd}
.tools{left:898px;top:24px;display:flex;gap:20px;align-items:center}
.cart{position:relative}
.badge{position:absolute;top:-12px;right:-14px;width:18px;height:18px;border-radius:50%;background:var(--orange);color:var(--white);font-size:10px;text-align:center;line-height:18px}
.hero-lead{top:306px;font-size:42px;font-weight:600;color:var(--white)}
.hero-title{top:362px;font-family:'Anton',sans-serif;font-size:51px;color:var(--white);letter-spacing:1px}
.btn-shop{left:487px;top:487px;width:183px;height:41px;background:var(--orange);color:#222;font-size:12px;font-weight:700;letter-spacing:1px;display:flex;align-items:center;justify-content:center;gap:6px}

/* products */
.products{top:653px;height:597px;background:var(--paper)}
.eyebrow{font-size:12px;font-weight:600;color:var(--orange-dark)}
.sec-title{font-family:'Overlock',sans-serif;font-weight:900;font-size:28px;color:var(--ink)}
.card{top:155px;width:267px;height:364px;background:var(--white);box-shadow:0 0 6px rgba(0,0,0,.08);text-align:center}
.card-photo{margin:6px;height:183px}
.stars{margin-top:20px;color:var(--orange);font-size:10px;letter-spacing:2px}
.card-name{margin-top:8px;font-weight:700;font-size:16px}
.price{margin-top:8px;color:var(--orange);font-size:12px;font-weight:600}
.btn-buy{display:inline-block;margin-top:14px;width:120px;height:30px;line-height:28px;border:1px solid #555;font-size:11px;font-weight:600}

/* about */
.about{top:1250px;height:437px;background:var(--white)}
.about h2,.why h2{font-family:'Overlock',sans-serif;font-weight:900;font-size:27px}
.about p{font-size:12px;line-height:20px;color:#333}
.btn-more{left:114px;top:286px;width:108px;height:39px;background:var(--orange);color:var(--white);font-size:11px;font-weight:700;display:flex;align-items:center;justify-content:center}
.about-photo{left:448px;top:68px;width:282px;height:283px;border:3px solid #111;border-radius:14px;background:radial-gradient(circle at 55% 55%,#5a3a10,#d9a11c 45%,#f1c232 80%)}
.why li{list-style:none;display:flex;align-items:center;gap:14px;font-size:12px;height:30px;color:#333}
.why h2 em{font-style:normal;color:var(--orange)}

/* query */
.query{top:1687px;height:586px;overflow:hidden}
.comb{position:absolute;inset:0;background:radial-gradient(ellipse at 20% 30%,#8a5a10,transparent 50%),radial-gradient(ellipse at 80% 70%,#7a4c0c,transparent 50%),linear-gradient(#3b2710,#2b1c0b)}
.query .eyebrow{color:var(--orange)}
.query .sec-title{color:var(--white);font-family:'Montserrat',sans-serif;font-weight:700;font-size:26px}
.field{height:35px;background:var(--white);font-size:11px;color:#333;padding:0 16px;line-height:35px}
.btn-send{left:256px;top:452px;width:647px;height:39px;background:var(--orange);color:var(--white);text-align:center;line-height:39px;font-size:13px;font-weight:600;letter-spacing:2px}

/* promises */
.promises{top:2273px;height:275px;background:var(--white)}
.promise{top:80px;width:320px;text-align:center}
.promise h3{margin-top:16px;font-size:12px;font-weight:600}
.promise p{margin-top:14px;font-size:11px;line-height:22px;color:var(--muted)}

/* subscribe */
.subscribe{top:2548px;height:278px;background:var(--olive);text-align:center;color:var(--white)}
.subscribe .eyebrow{color:var(--orange)}
.subscribe h2{font-family:'Montserrat',sans-serif;font-weight:700;font-size:27px}
.subscribe p{font-size:13px;line-height:22px}
.sub-form{left:265px;top:183px;width:629px;height:43px;border-radius:22px;background:var(--white);border:2px solid var(--orange);overflow:hidden;text-align:left}
.sub-form span{position:absolute;left:20px;top:12px;font-size:11px;color:var(--muted)}
.sub-btn{position:absolute;right:0;top:0;width:104px;height:100%;background:var(--orange);color:#222;font-size:11px;font-weight:700;text-align:center;line-height:39px;border-radius:20px}

/* footer */
.footer{top:2826px;height:358px;background:var(--dark);color:var(--white)}
.f-brand{font-size:30px;line-height:36px}
.f-desc{font-size:11px;line-height:20px;color:#ddd}
.f-head{font-size:12px;font-weight:600;color:var(--orange)}
.f-list li{list-style:none;font-size:11px;height:29px;line-height:29px;color:#eee}
.social{display:flex;gap:4px}
.social i{width:30px;height:30px;border-radius:50%;background:var(--orange);display:block}
.copyright{top:3184px;height:48px;background:var(--olive);color:var(--white);font-size:11px;text-align:center;line-height:48px}
</style>
</head>
<body>

<header class="hero">
  <div class="hero-photo" role="img" aria-label="Close-up photograph of honeybees crawling over wooden hive frames"></div>
  <div class="abs phone">
    <svg width="14" height="14" viewBox="0 0 24 24"><path fill="#fff" d="M6.6 10.8a15 15 0 006.6 6.6l2.2-2.2c.3-.3.7-.4 1-.2 1.1.4 2.3.6 3.6.6.6 0 1 .4 1 1V20c0 .6-.4 1-1 1A17 17 0 013 4c0-.6.4-1 1-1h3.5c.6 0 1 .4 1 1 0 1.3.2 2.5.6 3.6.1.3 0 .7-.2 1z"/></svg>
    555 014 2290
  </div>
  <div class="abs brand wordmark">Tarnfield<br>Hives LLC</div>
  <nav class="abs nav center">
    <span>HOME</span><span class="sep">-</span><span>ABOUT</span><span class="sep">-</span><span>SHOP</span><span class="sep">-</span><span>SERVICES</span><span class="sep">-</span><span>CONTACT</span>
  </nav>
  <div class="abs tools">
    <svg width="22" height="22" viewBox="0 0 24 24" fill="none" stroke="#fff" stroke-width="2.6"><circle cx="10" cy="10" r="6.5"/><path d="M15 15l6 6"/></svg>
    <svg width="22" height="22" viewBox="0 0 24 24" fill="none" stroke="#fff" stroke-width="2.2"><circle cx="12" cy="12" r="9.5"/><circle cx="12" cy="10" r="3.2"/><path d="M6 18.5c2-3 10-3 12 0"/></svg>
    <span class="cart">
      <svg width="24" height="22" viewBox="0 0 24 22" fill="#fff"><path d="M1 2h4l3 12h12l3-9H7" fill="none" stroke="#fff" stroke-width="2.2"/><circle cx="9" cy="19" r="2"/><circle cx="19" cy="19" r="2"/></svg>
      <span class="badge">0</span>
    </span>
  </div>
  <div class="abs hero-lead center">Tarnfield Hives Provide</div>
  <h1 class="abs hero-title center">2019 NUCS &amp; 2019 QUEENS</h1>
  <div class="abs btn-shop">SHOP NOW <span>›</span></div>
</header>

<section class="products">
  <div class="abs eyebrow center" style="top:46px">Prodcucts</div>
  <h2 class="abs sec-title center" style="top:70px">Featured Products</h2>
  <article class="abs card" style="left:131px">
    <div class="card-photo" role="img" aria-label="Single queen honeybee on a white background" style="background:radial-gradient(ellipse at 50% 55%,#b8742a 0,#e9e7e4 35%,#efefef 70%)"></div>
    <div class="stars">★★★★★</div>
    <div class="card-name">2019 Queen</div>
    <div class="price">$45.00</div>
    <div class="btn-buy">BUY NOW</div>
  </article>
  <article class="abs card" style="left:448px">
    <div class="card-photo" role="img" aria-label="Frame of honeycomb covered with worker bees" style="background:linear-gradient(135deg,#4a3414,#a07a3a 50%,#5a3e18)"></div>
    <div class="stars">★★★★★</div>
    <div class="card-name">2019 Nucs</div>
    <div class="price">$250.00</div>
    <div class="btn-buy">BUY NOW</div>
  </article>
  <article class="abs card" style="left:765px">
    <div class="card-photo" role="img" aria-label="Cluster of bees around a marked queen" style="background:linear-gradient(135deg,#3a2a14,#c88a2a 50%,#4a3218)"></div>
    <div class="stars">★★★★★</div>
    <div class="card-name">2019 Queen</div>
    <div class="price">$45.00</div>
    <div class="btn-buy">BUY NOW</div>
  </article>
</section>

<section class="about">
  <div class="abs eyebrow" style="left:114px;top:74px">Information</div>
  <h2 class="abs" style="left:114px;top:96px">About HoneyBees</h2>
  <svg class="abs" style="left:114px;top:142px" width="44" height="8" viewBox="0 0 44 8"><path d="M0 4q5.5-5 11 0t11 0 11 0 11 0" fill="none" stroke="var(--orange)" stroke-width="2"/></svg>
  <p class="abs" style="left:114px;top:162px;width:305px">Duis autem vel eum iriure dolor in hendrerit in vulputate velit esse molestie consequat, vel illum dolore eu feugiat nulla facilisis at vero eros et accumsan et iusto odio dignissim qui blandit praesent luptatum zzr</p>
  <div class="abs btn-more">Read More</div>
  <div class="abs about-photo" role="img" aria-label="Bees resting on golden honeycomb cells"></div>
  <div class="abs why" style="left:760px;top:72px">
    <h2>Why <em>Choose Us</em></h2>
    <ul style="margin-top:18px">
      <li><svg width="18" height="18" viewBox="0 0 18 18"><circle cx="9" cy="9" r="9" fill="var(--tick)"/><path d="M5 9.5l3 3 5-6" fill="none" stroke="#fff" stroke-width="2"/></svg>Duis autem vel eum iriure dolor in</li>
      <li><svg width="18" height="18" viewBox="0 0 18 18"><circle cx="9" cy="9" r="9" fill="var(--tick)"/><path d="M5 9.5l3 3 5-6" fill="none" stroke="#fff" stroke-width="2"/></svg>hendrerit in vulputate velit esse</li>
      <li><svg width="18" height="18" viewBox="0 0 18 18"><circle cx="9" cy="9" r="9" fill="var(--tick)"/><path d="M5 9.5l3 3 5-6" fill="none" stroke="#fff" stroke-width="2"/></svg>molestie consequat, vel illum</li>
      <li><svg width="18" height="18" viewBox="0 0 18 18"><circle cx="9" cy="9" r="9" fill="var(--tick)"/><path d="M5 9.5l3 3 5-6" fill="none" stroke="#fff" stroke-width="2"/></svg>dolore eu feugiat nulla facilisis at</li>
      <li><svg width="18" height="18" viewBox="0 0 18 18"><circle cx="9" cy="9" r="9" fill="var(--tick)"/><path d="M5 9.5l3 3 5-6" fill="none" stroke="#fff" stroke-width="2"/></svg>vero eros et accumsan et iusto odio</li>
      <li><svg width="18" height="18" viewBox="0 0 18 18"><circle cx="9" cy="9" r="9" fill="var(--tick)"/><path d="M5 9.5l3 3 5-6" fill="none" stroke="#fff" stroke-width="2"/></svg>dignissim qui blandit praesent</li>
    </ul>
  </div>
</section>

<section class="query">
  <div class="comb" role="img" aria-label="Dark honeycomb cells filled with honey"></div>
  <div class="abs eyebrow center" style="top:46px">Any Question</div>
  <h2 class="abs sec-title center" style="top:68px">Send your Query</h2>
  <div class="abs field" style="left:256px;top:146px;width:315px">Your Name</div>
  <div class="abs field" style="left:586px;top:146px;width:317px">Your Email</div>
  <div class="abs field" style="left:256px;top:206px;width:207px">Product</div>
  <div class="abs field" style="left:478px;top:206px;width:207px">Date</div>
  <div class="abs field" style="left:694px;top:206px;width:209px">Quantity</div>
  <div class="abs field" style="left:256px;top:267px;width:647px">Subject</div>
  <div class="abs field" style="left:256px;top:325px;width:647px;height:105px">Write your message here</div>
  <div class="abs btn-send">SEND YOUR QUERY</div>
</section>

<section class="promises">
  <div class="abs promise" style="left:105px">
    <svg width="50" height="50" viewBox="0 0 50 50" fill="none" stroke="#444" stroke-width="1.5"><path d="M25 3l5 5 7-1 1 7 6 4-3 6 3 6-6 4-1 7-7-1-5 5-5-5-7 1-1-7-6-4 3-6-3-6 6-4 1-7 7 1z"/><text x="25" y="29" font-size="9" text-anchor="middle" fill="#444" stroke="none" font-family="Montserrat,sans-serif">100%</text></svg>
    <h3>100% genuine Product</h3>
    <p>Mirum est notare quam littera gothica, quam nunc<br>putamus parum claram</p>
  </div>
  <div class="abs promise" style="left:417px">
    <svg width="50" height="50" viewBox="0 0 50 50" fill="none" stroke="#444" stroke-width="1.5"><ellipse cx="25" cy="28" rx="15" ry="12"/><path d="M18 38v5M32 38v5M20 14h10"/><circle cx="25" cy="27" r="4"/></svg>
    <h3>Money Back Guarantee</h3>
    <p>Mirum est notare quam littera gothica, quam nunc<br>putamus parum claram</p>
  </div>
  <div class="abs promise" style="left:727px">
    <svg width="50" height="50" viewBox="0 0 50 50" fill="none" stroke="#444" stroke-width="1.5"><circle cx="25" cy="20" r="8"/><path d="M13 22v-3a12 12 0 0124 0v3M12 44c1-9 6-12 13-12s12 3 13 12"/><rect x="10" y="19" width="4" height="7"/><rect x="36" y="19" width="4" height="7"/></svg>
    <h3>online SUpport 24/7</h3>
    <p>Mirum est notare quam littera gothica, quam nunc<br>putamus parum claram</p>
  </div>
</section>

<section class="subscribe">
  <div class="abs eyebrow center" style="top:30px">Special Offers For Subscriber</div>
  <h2 class="abs center" style="top:52px">10% Memebership Discount</h2>
  <p class="abs center" style="top:104px">Subscribe to our newsletters now and stay up to date with new collections, the latest lookbooks<br>and exclusive offers.</p>
  <div class="abs sub-form"><span>Type your email id</span><div class="sub-btn">SUBSCRIBE</div></div>
</section>

<footer class="footer">
  <div class="abs wordmark f-brand" style="left:114px;top:34px">Tarnfield<br>Hives LLC</div>
  <p class="abs f-desc" style="left:114px;top:138px;width:265px">Duis autem vel eum iriure dolor in hendrerit in vulputate velit esse molestie consequat, vel illum dolore eu feugiat nulla facilisis.</p>
  <div class="abs f-head" style="left:118px;top:210px">Follow Us</div>
  <div class="abs social" style="left:118px;top:240px"><i></i><i></i><i></i><i></i></div>

  <div class="abs" style="left:433px;top:94px">
    <div class="f-head">Opening Hours</div>
    <ul class="f-list" style="margin-top:14px"><li>Mon - Fri: 8AM - 10PM</li><li>Sat: 9AM-8PM</li><li>Sun: Closed</li></ul>
  </div>
  <div class="abs" style="left:663px;top:90px">
    <div class="f-head">Information</div>
    <ul class="f-list" style="margin-top:14px"><li>About Us</li><li>Delivery Information</li><li>Privacy Policy</li><li>Terms &amp; Conditions</li><li>Customer Service</li><li>Return Policy</li></ul>
  </div>
  <div class="abs" style="left:879px;top:86px">
    <div class="f-head">Account Info</div>
    <ul class="f-list" style="margin-top:14px"><li>My account</li><li>Wishlist</li><li>Newsletter</li><li>Order History</li><li>International Orders</li><li>Contact</li></ul>
  </div>
</footer>

<div class="abs copyright center">© All Rights Reserved - 2019</div>

</body>
</html>
```